Business Card Design Project

We are looking to redesign the logo, business card and stationary of one of our group companies - KESTRAL SUPPLY COMPANY LLC.

The company specialises in industrial PVC and CPVC Piping systems. It is situated in the Middle East and the focus is purely in this region.

The logo work is already completed. The file is uploaded for the reference.

We are looking for a clean minimalistic design for the business card.

regards
Ormund
Updates

Hello Everyone!

Thanks for submitting your designs. 

Yet to find the right design. Probably the below links will give you guys some more idea on what we would like.

Minimalist design with some creativity.

Ormund

http://plaincardgallery.example/inspiration/15-beautifully-minimal-business-cards

http://www.quietlayouthub.example/2011/11/14/30-minimalist-business-card-design/

http://www.firmpixelnotes.example/inspiration/minimal-business-cards/

Target Market(s)

Industrial users

Industry/Entity Type

Industrial

Requirements
Must have
• - Minimalistic design

- Back side of the card should include the manufacturer BRAVOLINE CANADA's decal. The file is upload for the reference

- Further information
Company Name:
KESTRAL SUPPLY COMPANY LLC
Address:
PO Box 9087, Sharjah Industrial Area 5, Qutrani Road
Sharjah, United Arab Emirates
Telephone:
+971-6-5018-392
Fax:
+977-6-5018-393
Email:
mail@ksc-holding.example

- FYI, Kestral Supply Company LLC is the authorised distributor for BRAVOLINE CANADA in the UAE. For further information on bravoline please visit the website www.bravoline.example

```html
<!DOCTYPE html>
<html lang="en">
<head>
<meta charset="utf-8">
<title>Kestral Supply Company LLC – Business Card</title>
<link rel="stylesheet" href="https://fonts.googleapis.com/css2?family=Arimo:ital,wght@0,400;0,700;1,400&family=Josefin+Sans:wght@400&family=Allura&display=swap">
<style>
  :root {
    --page-bg: #d9d4cc;
    --card-front: #5f6063;
    --card-back: #ffffff;
    --text-light: #ffffff;
    --pipes-light: #f4f4f4;
    --pipes-shade: #cfcfd0;
    --mark-fill: #3a6fb0;
    --faint-frame: #ececec;
    --faint-inner: #e3ebf6;
    --brand-text: #111111;
    --shadow: rgba(0, 0, 0, 0.25);
  }
  * { box-sizing: border-box; margin: 0; padding: 0; }
  html, body {
    width: 1200px;
    height: 900px;
    overflow: hidden;
    background: var(--page-bg);
  }
  .canvas {
    position: relative;
    width: 1200px;
    height: 900px;
  }
  .card {
    position: absolute;
    width: 640px;
    height: 365px;
    overflow: hidden;
    box-shadow: 0 6px 14px var(--shadow);
  }

  /* Front */
  .card-front {
    left: 110px;
    top: 70px;
    background: var(--card-front);
    color: var(--text-light);
  }
  .company-name {
    position: absolute;
    left: 56px;
    top: 92px;
    font-family: "Josefin Sans", sans-serif;
    font-weight: 400;
    font-size: 21px;
    letter-spacing: 5px;
    white-space: nowrap;
  }
  .pipes-area {
    position: absolute;
    left: 60px;
    bottom: 0;
    width: 212px;
    height: 150px;
    background: linear-gradient(90deg, var(--pipes-shade), var(--pipes-light) 45%, var(--pipes-shade));
  }
  .contact {
    position: absolute;
    right: 36px;
    top: 160px;
    text-align: right;
    font-family: "Arimo", sans-serif;
    font-style: normal;
    font-size: 14px;
    line-height: 20px;
  }
  .contact .person {
    font-family: "Allura", cursive;
    font-size: 30px;
    line-height: 36px;
    margin-bottom: 8px;
  }
  .contact .email { font-style: italic; }
  .mark-square {
    position: absolute;
    left: 428px;
    top: 270px;
    width: 30px;
    height: 30px;
    border-radius: 5px;
    background: var(--mark-fill);
  }

  /* Back */
  .card-back {
    left: 450px;
    top: 470px;
    background: var(--card-back);
  }
  .faint-square {
    position: absolute;
    left: -50px;
    top: -40px;
    width: 290px;
    height: 290px;
    border-radius: 60px;
    border: 26px solid var(--faint-frame);
    background: var(--faint-inner);
  }
  .manufacturer {
    position: absolute;
    right: 48px;
    bottom: 62px;
    display: flex;
    align-items: center;
    gap: 6px;
    font-family: "Arimo", sans-serif;
    font-weight: 700;
    font-size: 17px;
    color: var(--brand-text);
  }
  .manufacturer .brand-square {
    width: 18px;
    height: 18px;
    background: var(--brand-text);
  }
</style>
</head>
<body>
<main class="canvas">
  <section class="card card-front" aria-label="Business card front">
    <h1 class="company-name">KESTRAL SUPPLY COMPANY, LLC</h1>

    <div class="pipes-area" role="img" aria-label="Illustration of four white pipe cylinders of different heights"></div>

    <span class="mark-square" aria-hidden="true"></span>

    <address class="contact">
      <p class="person">Ormund Surname</p>
      <p>PO Box 9087</p>
      <p>Sharjah Industrial Area 5, Qutrani Road</p>
      <p>Sharjah, United Arab Emirates</p>
      <p>+971-6-5018-392 • T</p>
      <p>+977-6-5018-393 • F</p>
      <p class="email">mail@ksc-holding.example</p>
    </address>
  </section>

  <section class="card card-back" aria-label="Business card back">
    <div class="faint-square" aria-hidden="true"></div>
    <div class="manufacturer">
      <span class="brand-square" aria-hidden="true"></span>
      <span>Bravoline Canada</span>
    </div>
  </section>
</main>
</body>
</html>
```